Wordpress Design For Virtual Assistant

I need a website design for my virtual assistant company, BrimLoop. I would like to have a landing page, an about page, a page to list my services, contact us and FAQ. a blog page would be great as well.

It needs to be a modern, professional but fun look. Simple and easy to read and navigate. Colors used need to match the logo colors exactly with the red color being used only as a highlight/accept color.

I have uploaded an overview of BrimLoop as well as my logo, copy of business card and stationary to give you an idea of the design style I prefer.

Industry/Entity Type

It Company

Coding

Coded - Design and coding required

Font styles to use
Sans Serif

Requirements
Must have
• Color scheme with exact logo colors
Nice to have
• www.quorvane.com/ can be used as an style inspiration

```html
<!DOCTYPE html>
<html lang="en">
<head>
<meta charset="utf-8">
<title>BrimLoop – Virtual Assistant Company</title>
<link href="https://fonts.googleapis.com/css2?family=Open+Sans:wght@400;600;700&display=swap" rel="stylesheet">
<style>
:root{
  --accent:#c8502b;
  --teal:#4b9aa9;
  --green:#8bbb2b;
  --navy:#1f3a68;
  --ink:#333333;
  --muted:#5a5a5a;
  --light:#f6f7f8;
  --dark:#1d1d22;
  --footer:#f1f1f1;
  --bar:#2b2b2b;
}
*{box-sizing:border-box;margin:0;padding:0}
html,body{width:1200px;height:2917px;overflow:hidden}
body{font-family:"Open Sans",Arial,sans-serif;color:var(--ink);background:#fff;position:relative}
a{color:inherit;text-decoration:none}

/* header */
.site-header{position:absolute;top:0;left:0;width:1200px;height:100px;background:#fff;border-top:4px solid transparent;
  border-image:linear-gradient(90deg,#fff 35%,var(--accent) 35%,var(--accent) 70%,var(--teal) 70%) 1}
.brand{position:absolute;left:98px;top:30px;display:flex;align-items:center;gap:10px;font-size:30px;font-weight:700;color:var(--navy)}
.brand-dot{width:16px;height:16px;border-radius:50%;background:var(--accent)}
.main-nav{position:absolute;top:40px;left:422px;display:flex;gap:0;font-size:14px;font-weight:600;color:#333}
.main-nav a{margin-right:38px}
.main-nav a.active{color:var(--accent)}
.nav-cta{position:absolute;left:968px;top:32px;width:134px;height:38px;border-radius:19px;background:var(--teal);color:#fff;font-size:13px;font-weight:600;display:flex;align-items:center;justify-content:center}

/* hero */
.hero{position:absolute;top:100px;left:0;width:1200px;height:543px}
.hero-photo{position:absolute;inset:0;background:linear-gradient(120deg,#5d7080 0%,#3d5566 40%,#5a6a74 70%,#87939a 100%)}
.hero-text{position:absolute;top:290px;left:0;width:1200px;text-align:center;color:#fff}
.hero-text h1{font-size:62px;font-weight:700;letter-spacing:2px;line-height:1}
.hero-text p{font-size:25px;font-weight:700;margin-top:14px;letter-spacing:1px}
.hero-arrow{position:absolute;top:236px}
.hero-arrow.prev{left:48px}.hero-arrow.next{right:48px}

/* section titles */
.section-title{text-align:center;font-weight:400;font-size:32px;color:#222}
.section-title span{color:var(--navy);font-weight:600}
.section-lead{text-align:center;font-size:12px;line-height:21px;color:var(--muted)}

/* services */
.services{position:absolute;top:643px;left:0;width:1200px;height:452px;background:var(--light)}
.services .panel{position:absolute;left:32px;top:10px;width:1136px;height:430px;background:#fff;box-shadow:0 0 20px rgba(0,0,0,.05)}
.services .section-title{position:absolute;top:70px;width:1200px}
.services .section-lead{position:absolute;top:118px;width:1200px}
.service{position:absolute;top:185px;width:250px;text-align:center}
.service-icon{width:100px;height:100px;border-radius:50%;background:var(--accent);margin:0 auto;display:flex;align-items:center;justify-content:center}
.service h3{font-size:17px;font-weight:400;margin-top:22px;color:#333}
.service p{font-size:12px;line-height:19px;color:var(--muted);margin-top:10px}
.read-more{display:block;font-size:12px;color:var(--accent);margin-top:12px;font-weight:600}

/* welcome */
.welcome{position:absolute;top:1095px;left:0;width:1200px;height:638px;background:#fff}
.welcome .section-title{position:absolute;top:112px;width:1200px;font-size:35px}
.welcome .section-title span{color:var(--teal);font-weight:400}
.welcome .section-lead{position:absolute;top:170px;left:140px;width:920px;font-size:11px;line-height:21px}
.feature{position:absolute;top:260px;width:318px;height:328px}
.feature-photo{height:190px}
.feature-body{height:138px;color:#fff;text-align:center;padding:14px 30px 0}
.feature-body h3{font-size:20px;font-weight:600;letter-spacing:.5px}
.feature-body p{font-size:11px;line-height:20px;margin-top:8px}
.op .feature-body{background:var(--green)}
.mk .feature-body{background:var(--accent)}
.cp .feature-body{background:var(--teal)}

/* conclusion */
.conclusion{position:absolute;top:1733px;left:0;width:1200px;height:454px;background:linear-gradient(180deg,#1b1c20 0%,#25262b 50%,#4a2e22 100%)}
.conclusion h2{position:absolute;top:140px;width:1200px;text-align:center;color:#fff;font-size:40px;font-weight:600;letter-spacing:1px}
.conclusion p{position:absolute;top:205px;left:150px;width:900px;text-align:center;color:#eee;font-size:13px;line-height:25px}
.btn-outline{position:absolute;left:490px;top:312px;width:220px;height:48px;border:1px solid #ddd;border-radius:24px;color:#fff;font-size:20px;display:flex;align-items:center;justify-content:center}

/* blog */
.blog{position:absolute;top:2187px;left:0;width:1200px;height:453px;background:#fff}
.blog .section-title{position:absolute;top:108px;width:1200px;font-size:28px;color:#333}
.post{position:absolute;top:185px;width:270px}
.post-date{position:absolute;left:0;top:0;width:42px;text-align:center;font-size:12px}
.post-date .d{background:var(--accent);color:#fff;height:20px;line-height:20px}
.post-date .m{background:#eee;color:#333;height:22px;line-height:22px;font-size:14px}
.post h3{margin-left:50px;font-size:16px;font-weight:400;color:#666;line-height:24px}
.post p{font-size:11px;line-height:21px;color:#555;margin-top:14px}
.post .more{display:flex;align-items:center;gap:6px;font-size:12px;color:var(--navy);margin-top:20px;font-weight:600}
.post .more i{width:12px;height:12px;background:var(--navy);display:inline-block}

/* footer */
.site-footer{position:absolute;top:2640px;left:0;width:1200px;height:227px;background:var(--footer)}
.footer-col{position:absolute;top:38px}
.footer-col h4{font-size:15px;font-weight:400;color:#333;letter-spacing:.5px}
.contact-line{display:flex;gap:16px;font-size:13px;line-height:21px;color:#444;margin-top:16px}
.event p{font-size:11px;line-height:18px;color:#444;margin-top:16px}
.event span{font-size:11px;color:var(--navy);display:block;margin-top:4px}
.field{width:228px;height:42px;background:#fff;border:1px solid #e2e2e2;font-size:11px;color:#444;padding:13px 14px}
.subscribe{position:absolute;left:134px;top:2px;width:90px;height:34px;background:var(--navy);color:#fff;font-size:11px;font-weight:700;display:flex;align-items:center;justify-content:center}
.footer-brand{position:absolute;left:972px;top:60px;display:flex;align-items:center;gap:8px;font-size:26px;font-weight:700;color:var(--navy)}
.socials{position:absolute;left:950px;top:140px;display:flex;gap:10px}
.socials i{width:22px;height:22px;display:block}
.copyright{position:absolute;top:2867px;left:0;width:1200px;height:50px;background:var(--bar);color:#ddd;font-size:11px;text-align:center;line-height:50px}
</style>
</head>
<body>

<header class="site-header">
  <a class="brand" href="#"><span class="brand-dot"></span>BrimLoop</a>
  <nav class="main-nav">
    <a class="active" href="#">HOME</a><a href="#">ABOUT US</a><a href="#">SERVICES</a><a href="#">FAQ</a><a href="#">BLOG</a><a href="#">CONTACT US</a>
  </nav>
  <a class="nav-cta" href="#">CONCLUSION</a>
</header>

<section class="hero">
  <div class="hero-photo" role="img" aria-label="Two smiling colleagues discussing work at an office desk"></div>
  <svg class="hero-arrow prev" width="34" height="64" viewBox="0 0 34 64"><path d="M30 2 4 32l26 30" fill="none" stroke="#fff" stroke-width="2"/></svg>
  <svg class="hero-arrow next" width="34" height="64" viewBox="0 0 34 64"><path d="M4 2l26 30L4 62" fill="none" stroke="#fff" stroke-width="2"/></svg>
  <div class="hero-text">
    <h1>BRIMLOOP</h1>
    <p>VIRTUAL ASSISTANT COMPANY</p>
  </div>
</section>

<section class="services">
  <div class="panel"></div>
  <h2 class="section-title">OUR <span>SERVICES</span></h2>
  <p class="section-lead">Lorem ipsum dolor sit amet, consectetur adipiscing elit, sed do eiusmod tempor incididunt ut labore et dolore magna aliqua.<br>Ut enim ad minim veniam, quis nostrud exercitation ullamco laboris nisi ut aliquip</p>

  <div class="service" style="left:81px">
    <div class="service-icon"><svg width="38" height="38" viewBox="0 0 38 38"><path d="M6 12h9a4 4 0 1 1 8 0h9v9a4 4 0 1 0 0 8v5H6z" fill="#fff"/></svg></div>
    <h3>Virtual Organization</h3>
    <p>Nemo enim ipsam voluptatem quia voluptas sit aspernatur aut odit aut fugit, sed quia consequuntur magni</p>
    <a class="read-more" href="#">READ MORE</a>
  </div>
  <div class="service" style="left:346px">
    <div class="service-icon"><svg width="42" height="36" viewBox="0 0 42 36"><circle cx="21" cy="9" r="6" fill="#fff"/><circle cx="8" cy="13" r="4.5" fill="#fff"/><circle cx="34" cy="13" r="4.5" fill="#fff"/><path d="M11 32a10 10 0 0 1 20 0zM0 30a8 8 0 0 1 14-5l-2 5zM42 30a8 8 0 0 0-14-5l2 5z" fill="#fff"/></svg></div>
    <h3>Business Consulting</h3>
    <p>Nemo enim ipsam voluptatem quia voluptas sit aspernatur aut odit aut fugit, sed quia consequuntur magni</p>
    <a class="read-more" href="#">READ MORE</a>
  </div>
  <div class="service" style="left:610px">
    <div class="service-icon"><svg width="38" height="38" viewBox="0 0 38 38"><rect x="4" y="7" width="30" height="27" rx="2" fill="none" stroke="#fff" stroke-width="3"/><path d="M4 14h30M11 3v7M27 3v7" stroke="#fff" stroke-width="3"/><path d="M10 19h4v4h-4zM17 19h4v4h-4zM24 19h4v4h-4zM10 26h4v4h-4zM17 26h4v4h-4z" fill="#fff"/></svg></div>
    <h3>Event Planning</h3>
    <p>Nemo enim ipsam voluptatem quia voluptas sit aspernatur aut odit aut fugit, sed quia consequuntur magni</p>
    <a class="read-more" href="#">READ MORE</a>
  </div>
  <div class="service" style="left:869px">
    <div class="service-icon"><svg width="40" height="40" viewBox="0 0 40 40"><path d="M36 4c-2-2-6 0-9 3l-6 6-14-4-3 3 11 7-5 5-5-1-2 2 6 3 3 6 2-2-1-5 5-5 7 11 3-3-4-14 6-6c3-3 5-7 3-9z" fill="#fff"/></svg></div>
    <h3>Travel Arrangements</h3>
    <p>Nemo enim ipsam voluptatem quia voluptas sit aspernatur aut odit aut fugit, sed quia consequuntur magni</p>
    <a class="read-more" href="#">READ MORE</a>
  </div>
</section>

<section class="welcome">
  <h2 class="section-title">Welcome To <span>BrimLoop</span></h2>
  <p class="section-lead">Lorem ipsum dolor sit amet, consectetur adipiscing elit, sed do eiusmod tempor incididunt ut labore et dolore magna aliqua. Ut enim ad minim veniam, quis nostrud exercitation ullamco laboris nisi ut aliquip ex ea commodo consequat. Duis aute irure dolor in reprehenderit in voluptate velit esse cillum dolore eu fugiat nulla pariatur. Excepteur sint occaecat cupidatat non proident, sunt in culpa qui officia deserunt mollit anim id est laborum.</p>

  <article class="feature op" style="left:100px">
    <div class="feature-photo" role="img" aria-label="Red dart striking the centre of a dartboard" style="background:linear-gradient(135deg,#dfe4ec,#8b97ad)"></div>
    <div class="feature-body"><h3>OPERATIONS</h3><p>Mara Quell is the registered agent and will supervise all day to day operations until the time comes for expansion. Virtual applications</p></div>
  </article>
  <article class="feature mk" style="left:441px">
    <div class="feature-photo" role="img" aria-label="Business team figures below a rising red growth arrow" style="background:linear-gradient(180deg,#c9ccd0,#e8e8e8)"></div>
    <div class="feature-body"><h3>MARKETING</h3><p>Our target market is small business owners/entrepreneurs in the Dallas area between the ages of 30-65 who have little to no online</p></div>
  </article>
  <article class="feature cp" style="left:782px">
    <div class="feature-photo" role="img" aria-label="Business handshake in front of a blue digital city skyline" style="background:linear-gradient(135deg,#1f3c5e,#6d8fb0)"></div>
    <div class="feature-body"><h3>COMPETITION</h3><p>The world today is moving away from traditional ways of doing business and toward utilizing virtual, more efficient ways to get things</p></div>
  </article>
</section>

<section class="conclusion" role="img" aria-label="Dark mountain landscape at dusk behind the closing message">
  <h2>BRIMLOOP CONCLUSION</h2>
  <p>At BrimLoop, we are committed to become your virtual resource by providing quality, cutting edge services to expand your business virtually and save your valuable time. The time to act is now! Start increasing your bottom line, stay ahead of your competitors and let us integrate technology to work for you. Stop falling farther behind and give your business a huge boost. We will help you get there.</p>
  <a class="btn-outline" href="#">CONCLUSION</a>
</section>

<section class="blog">
  <h2 class="section-title">LATEST BLOG</h2>
  <article class="post" style="left:97px">
    <div class="post-date"><div class="d">03</div><div class="m">Sep</div></div>
    <h3>Nemo enim ipsam volup quia voluptas sit</h3>
    <p>Lorem ipsum dolor sit amet, consectetur adipiscing elit, sed do eiusmod tempor incididunt ut labore et dolore magna aliqua. Ut enim ad minim veniam, quis nostrud exercitation ullamco laboris nisi ut aliquip ex ea commodo consequat.</p>
    <a class="more" href="#">READ MORE <i></i></a>
  </article>
  <article class="post" style="left:457px">
    <div class="post-date"><div class="d">03</div><div class="m">Sep</div></div>
    <h3>Nemo enim ipsam volup quia voluptas sit</h3>
    <p>Lorem ipsum dolor sit amet, consectetur adipiscing elit, sed do eiusmod tempor incididunt ut labore et dolore magna aliqua. Ut enim ad minim veniam, quis nostrud exercitation ullamco laboris nisi ut aliquip ex ea commodo consequat.</p>
    <a class="more" href="#">READ MORE <i></i></a>
  </article>
  <article class="post" style="left:834px">
    <div class="post-date"><div class="d">03</div><div class="m">Sep</div></div>
    <h3>Nemo enim ipsam volup quia voluptas sit</h3>
    <p>Lorem ipsum dolor sit amet, consectetur adipiscing elit, sed do eiusmod tempor incididunt ut labore et dolore magna aliqua. Ut enim ad minim veniam, quis nostrud exercitation ullamco laboris nisi ut aliquip ex ea commodo consequat.</p>
    <a class="more" href="#">READ MORE <i></i></a>
  </article>
</section>

<footer class="site-footer">
  <div class="footer-col" style="left:99px">
    <h4>CONTACT US</h4>
    <div class="contact-line"><svg width="16" height="22" viewBox="0 0 16 22"><path d="M8 0a8 8 0 0 0-8 8c0 6 8 14 8 14s8-8 8-14a8 8 0 0 0-8-8z" fill="var(--accent)"/><circle cx="8" cy="8" r="3" fill="#fff"/></svg><div>BrimLoop<br>418 West Harlow Avenue,<br>Denbury OHIO 43210, USA.</div></div>
    <div class="contact-line" style="margin-top:14px"><svg width="16" height="16" viewBox="0 0 16 16"><path d="M3 1l3 3-2 2c1 2 4 5 6 6l2-2 3 3-2 2C7 15 1 9 1 3z" fill="none" stroke="var(--accent)" stroke-width="1.4"/></svg><div>+1 04 2281 6630</div></div>
    <div class="contact-line" style="margin-top:6px"><svg width="16" height="14" viewBox="0 0 16 14"><rect x="1" y="2" width="14" height="10" fill="none" stroke="var(--accent)" stroke-width="1.4"/><path d="M1 2l7 6 7-6" fill="none" stroke="var(--accent)" stroke-width="1.4"/></svg><div>info@brimloop.biz</div></div>
  </div>
  <div class="footer-col event" style="left:391px;width:260px">
    <h4>RECENT EVENTS</h4>
    <p>Lorem ipsum dolor sit amet, consectetur adipiscing elit, sed do eiusmod<span>3 days ago</span></p>
    <p>Lorem ipsum dolor sit amet, consectetur adipiscing elit, sed do eiusmod<span>3 days ago</span></p>
  </div>
  <div class="footer-col" style="left:667px">
    <h4>SIGN UP FOR NEWSLETTER</h4>
    <div class="field" style="margin-top:14px">Enter Name</div>
    <div style="position:relative;margin-top:4px"><div class="field">Enter Email</div><span class="subscribe">SUBSCRIBE</span></div>
  </div>
  <div class="footer-brand"><span class="brand-dot"></span>BrimLoop</div>
  <div class="socials">
    <i style="background:#d34836"></i><i style="background:#3b5998"></i><i style="background:#1da1f2"></i><i style="background:#0e76a8"></i><i style="background:#c4302b"></i>
  </div>
</footer>
<div class="copyright">©2015 - 2016 BRIMLOOP., All Rights Reserved.</div>

</body>
</html>
```